Business Card for beauty technology startup

Design Glowmi Business Card for a Beauty, based on the website identity and colors (https://www.glowmi-example.com).
Glowmi is a beauty tech startup that gathers helpful product info for beauty lovers and consumers (such as availability on stores, price range and product reviews) for makeup products. The card design must be young, colorful but clean, and very modern.

Target Market(s)

woman, 15-35

Industry/Entity Type

Cosmetics

Contact Information for Business Card

Full Name, address, phone

Font styles to use
Other font styles liked:
• Advent Pro

Colors
e34297
86cfc6
ffffff
5c5c5c
e8e8e8
e667a6
b2b2b2

Requirements
Must have
• One full colored side with a creative design and another with card info
• Use Color palette: #95C5C5 and/or #D38AA5
• Use fonts: Advent Pro
• Use website identity: https://www.glowmi-example.com
Nice to have
• If needed extra font: Roboto

```html
<!DOCTYPE html>
<html lang="en">
<head>
<meta charset="UTF-8">
<title>Glowmi Business Card</title>
<link rel="stylesheet" href="https://fonts.googleapis.com/css2?family=Advent+Pro:wght@300;400&family=Roboto:wght@400&family=Roboto+Condensed:wght@500&display=swap">
<style>
  :root {
    --backdrop: #2a2a2a;
    --card-white: #f5f5f5;
    --brand-pink: #b97f93;
    --band-grey: #b2b2b2;
    --text-grey: #555555;
    --divider: #8a8a8a;
    --white: #ffffff;
  }
  * { margin: 0; padding: 0; box-sizing: border-box; }
  html, body { width: 1200px; height: 960px; overflow: hidden; }
  body { background: var(--backdrop); position: relative; font-family: "Roboto", Arial, sans-serif; }

  .card { position: absolute; width: 600px; height: 342px; border-radius: 18px; overflow: hidden; }
  .card-front { left: 314px; top: 113px; background: var(--card-white); }
  .card-back { left: 311px; top: 472px; background: var(--brand-pink); }

  .brand-mark { position: absolute; left: 129px; top: 77px; width: 96px; height: 96px; border: 4px solid var(--brand-pink); border-radius: 50%; }
  .brand-name { position: absolute; left: 76px; top: 194px; width: 202px; text-align: center; font-family: "Advent Pro", Arial, sans-serif; font-weight: 300; font-size: 42px; letter-spacing: 6px; color: var(--brand-pink); line-height: 1; }

  .divider { position: absolute; left: 303px; top: 62px; width: 2px; height: 202px; background: linear-gradient(to bottom, transparent, var(--divider) 20%, var(--divider) 80%, transparent); }

  .contact { position: absolute; left: 340px; top: 66px; color: var(--text-grey); font-size: 14.5px; line-height: 19px; }
  .person-name { font-family: "Roboto Condensed", Arial, sans-serif; font-weight: 500; font-size: 20px; color: var(--brand-pink); line-height: 24px; }
  .person-role { font-family: "Roboto Condensed", Arial, sans-serif; font-weight: 500; font-size: 15px; line-height: 20px; margin-bottom: 10px; }
  .address { margin-bottom: 9px; }
  .contact-list { list-style: none; }
  .contact-list li { display: flex; align-items: center; gap: 9px; }
  .contact-list svg { width: 14px; height: 14px; fill: var(--brand-pink); flex: none; }

  .web-band { position: absolute; left: 0; top: 299px; width: 600px; height: 30px; display: flex; }
  .web-band-main { width: 466px; background: var(--brand-pink); display: flex; align-items: center; justify-content: center; padding-left: 0; }
  .web-band-end { flex: 1; background: var(--band-grey); position: relative; }
  .band-mark { position: absolute; left: 2px; top: 1px; width: 28px; height: 28px; border: 2px solid var(--white); border-radius: 50%; }
  .web-address { font-family: "Advent Pro", Arial, sans-serif; font-size: 15px; letter-spacing: 3px; color: var(--white); margin-left: 100px; }

  .back-mark { position: absolute; left: 238px; top: 68px; width: 124px; height: 124px; border: 5px solid var(--white); border-radius: 50%; }
  .back-name { position: absolute; left: 0; top: 216px; width: 600px; text-align: center; font-family: "Advent Pro", Arial, sans-serif; font-weight: 300; font-size: 38px; letter-spacing: 6px; color: var(--white); line-height: 1; }
  .back-web { position: absolute; left: 0; top: 294px; width: 600px; text-align: center; font-family: "Advent Pro", Arial, sans-serif; font-size: 15px; letter-spacing: 3px; color: var(--white); }
</style>
</head>
<body>
  <section class="card card-front">
    <div class="brand-mark"></div>
    <div class="brand-name">GLOWMI</div>
    <div class="divider"></div>

    <div class="contact">
      <div class="person-name">MAYA LINDQVIST</div>
      <div class="person-role">CEO/FOUNDER</div>
      <div class="address">214 Willow Crest Road<br>Fairview, Oregon 97024</div>
      <ul class="contact-list">
        <li><svg viewBox="0 0 24 24"><path d="M6.6 10.8a15.1 15.1 0 0 0 6.6 6.6l2.2-2.2c.3-.3.7-.4 1-.2 1.1.4 2.3.6 3.6.6.6 0 1 .4 1 1V20c0 .6-.4 1-1 1A17 17 0 0 1 3 4c0-.6.4-1 1-1h3.5c.6 0 1 .4 1 1 0 1.3.2 2.5.6 3.6.1.3 0 .7-.2 1z"/></svg>555 201 4418</li>
        <li><svg viewBox="0 0 24 24"><path d="M7 1h10a2 2 0 0 1 2 2v18a2 2 0 0 1-2 2H7a2 2 0 0 1-2-2V3a2 2 0 0 1 2-2zm0 3v14h10V4zm5 15.5a1.2 1.2 0 1 0 0 2.4 1.2 1.2 0 0 0 0-2.4z"/></svg>555 307 6291</li>
        <li><svg viewBox="0 0 24 24"><path d="M6 2h12v5H6zM3 8h18a2 2 0 0 1 2 2v7h-4v5H5v-5H1v-7a2 2 0 0 1 2-2zm4 8v4h10v-4z"/></svg>555 412 8830</li>
        <li><svg viewBox="0 0 24 24"><path d="M2 5h20v14H2zm2 2v.5l8 5 8-5V7zm0 2.8V17h16V9.8l-8 5z"/></svg>info@glowmi-example.com</li>
      </ul>
    </div>

    <div class="web-band">
      <div class="web-band-main"><span class="web-address">www.glowmi-example.com</span></div>
      <div class="web-band-end"><div class="band-mark"></div></div>
    </div>
  </section>

  <section class="card card-back">
    <div class="back-mark"></div>
    <div class="back-name">GLOWMI</div>
    <div class="back-web">www.glowmi-example.com</div>
  </section>
</body>
</html>
```